Design four banner ads for our upcoming revamped website

We need four banner ads for our website.

The link of our website is http://beta.mervatrade.com/

The banners will appear under the "Promotions" tab which is currently exhibiting placeholder images.

The titles for each of the banner ads are as follow:
1) Double Credit Chance
2) Capital Protection Scheme
3) Trade Bonus
4) 2.5% Annual Interest

Target Market(s)

forex traders

Requirements
Must have
• The banners must adhere and blend with the website existing theme
Should not have
• Please do not use any human figures in the banner or pictures of humans waving around cash.

```html
<!DOCTYPE html>
<html lang="en">
<head>
<meta charset="utf-8">
<title>Double Credit Chance</title>
<link rel="stylesheet" href="https://fonts.googleapis.com/css2?family=Open+Sans:wght@400;700&display=swap">
<style>
  :root {
    --sky-top: #a6d0ef;
    --sky-mid: #cfe6f7;
    --sky-low: #f2f8fd;
    --brand-orange: #f4841f;
    --table-light: #c88d52;
    --table-dark: #a0683a;
    --glass-light: #eaf1f6;
    --coin-copper: #b98a62;
    --coin-silver: #d3c6b8;
    --glass-neck: #8d6f53;
    --cash-pink: #d5c2c2;
    --cash-green: #aea28c;
    --glass-base: #6e4c34;
  }
  * { margin: 0; padding: 0; box-sizing: border-box; }
  html, body { width: 1200px; height: 522px; overflow: hidden; }
  .promo-banner {
    position: relative;
    width: 1200px;
    height: 522px;
    overflow: hidden;
    background: linear-gradient(180deg, var(--sky-top) 0%, var(--sky-mid) 45%, var(--sky-low) 78%, #ffffff 100%);
    font-family: "Open Sans", Arial, sans-serif;
  }
  .promo-title {
    position: absolute;
    left: 130px;
    top: 139px;
    color: var(--brand-orange);
    line-height: 1;
    white-space: nowrap;
  }
  .promo-title__lead {
    display: block;
    font-weight: 700;
    font-size: 116px;
    letter-spacing: 1px;
  }
  .promo-title__rest {
    display: block;
    margin-top: -6px;
    font-weight: 400;
    font-size: 84px;
    letter-spacing: 0;
  }
  .hourglass-visual {
    position: absolute;
    left: 931px;
    top: 0;
    width: 228px;
    height: 506px;
    border-radius: 40px 40px 60px 60px;
    background:
      radial-gradient(ellipse 42% 16% at 50% 26%, var(--coin-copper) 0%, rgba(185,138,98,0) 100%),
      radial-gradient(ellipse 44% 18% at 50% 80%, var(--cash-pink) 0%, rgba(213,194,194,0) 100%),
      linear-gradient(180deg,
        var(--glass-light) 0%,
        var(--glass-light) 12%,
        var(--coin-silver) 18%,
        var(--coin-copper) 30%,
        var(--glass-neck) 46%,
        var(--glass-light) 54%,
        var(--glass-light) 64%,
        var(--cash-pink) 74%,
        var(--cash-green) 88%,
        var(--glass-base) 100%);
    opacity: 0.9;
  }
  .tabletop {
    position: absolute;
    left: 0;
    bottom: 0;
    width: 100%;
    height: 20px;
    background: linear-gradient(180deg, var(--table-light) 0%, var(--table-dark) 100%);
  }
</style>
</head>
<body>
  <main class="promo-banner">
    <h1 class="promo-title">
      <span class="promo-title__lead">DOUBLE</span>
      <span class="promo-title__rest">CREDIT CHANCE</span>
    </h1>
    <div class="hourglass-visual" role="img" aria-label="Photo of a glass hourglass: coins pile in the top bulb and fall through the neck, turning into stacks of banknotes in the bottom bulb, showing money growing over time"></div>
    <div class="tabletop" role="img" aria-label="Wooden tabletop the hourglass stands on"></div>
  </main>
</body>
</html>
```